Seminar Flyer

We would like a flyer describing a seminar we will be presenting to window cleaners. The seminar topic is Glass Restoration and will include discussions on types of glass, types of glass damage and solutions. I am including the following (sample) description:
"Spend a day with The PaneMaven and learn how you can benefit from learning "Glass Restoration" and the many benefits to offering this service to your clients.
Before investing a lot of "time and money" in ANY Glass Restoration System, learn what Glass Restoration is all about and how you can turn a small investment into a very profitable business. And, this new business can be easily expanded into several other related business's.
Ready to expand your business and make some great money?
"DON'T WAIT" - Start offering your clients Glass Restoration Services.
"Glass Restoration" is one of the most profitable "Add-On" businesses for the window cleaning industry and you now have an opportunity to learn from one of the industry
leaders. Lyle Brandt will be offering a full day "hands-on" seminar on Glass Restoration.
The seminar will cover:
Glass Types
Glass Damage
Glass Coatings
Glass Distortion & Breakage
Glass Restoration Systems
Glass Restoration Procedures
Customer Expectations
Marketing and Pricing a job
Hands on demonstrations
And much much more.....
And did I mention it will cover "Glass"?
This full day seminar will be presented by Lyle Brandt and sponsored by the H.Morwick Company at their facility in Carson, California.
Space will be limited, so you must register to attend, but the seminar and lunch is FREE.
This all day seminar will also cover discussions on:
Hard Water Spot Removal and methods for removing.
What exactly is "Tin Etch Haze" and how to prevent or remove it easily.
Minor scratch removal (light scratches and metal marks)
Tempered Glass Defects - Waivers and precautions
Excess Scratch removal (tempered Glass scratching)
Graffiti Removal (major scratch and acid etch damage)
Additional Money Makers:
Anti-Graffiti Film Application
- An easy add on business for glass restoration businesses
Hard Water Spot Removal and Glass Sealant
- An easy add on business for window cleaning businesses
Window Frame Restoration and Treatment
- An easy add on business for window cleaning businesses"
Lyle Brandt, the President of The Brandt Company, is well known in the window cleaning industry as "PaneMaven", so we want to make sure that branding is included in the flyer.
PLEASE NOTE: The flyer will be distributed as an e-mail attachment so the flyer itself will not have any specific information regarding dates and location.
Target Market(s)
Window Cleaners; small business owners.
Industry/Entity Type
Window Cleaning

```html
<!DOCTYPE html>
<html lang="en">
<head>
<meta charset="utf-8">
<title>Glass Restoration Seminar</title>
<link href="https://fonts.googleapis.com/css2?family=Titan+One&family=Arimo:wght@700&display=swap" rel="stylesheet">
<style>
  :root {
    --page: #ffffff;
    --blue: #1f6fc2;
    --blue-deep: #1558a6;
    --lime: #d2df2c;
    --teal: #6fcbc6;
    --navy: #1b2470;
    --title-yellow: #fff22e;
    --title-line: #0d1a4a;
  }
  html, body {
    margin: 0;
    padding: 0;
    width: 1200px;
    height: 900px;
    overflow: hidden;
    background: var(--page);
  }
  .canvas {
    position: relative;
    width: 1200px;
    height: 900px;
    background: var(--page);
  }
  .flyer {
    position: absolute;
    left: 280px;
    top: 0;
    width: 644px;
    height: 900px;
    font-family: "Arimo", Arial, sans-serif;
    font-weight: 700;
    color: var(--navy);
    overflow: hidden;
  }
  .band { position: absolute; left: 0; width: 644px; }
  .band--header { top: 0; height: 184px; background: linear-gradient(180deg, var(--blue) 0%, var(--blue-deep) 100%); }
  .band--intro { top: 184px; height: 100px; background: var(--lime); }
  .band--call { top: 284px; height: 120px; background: var(--teal); }
  .band--body { top: 404px; height: 436px; background: var(--lime); }
  .band--footer { top: 840px; height: 60px; background: var(--blue); }

  .title {
    position: absolute;
    margin: 0;
    font-family: "Titan One", "Arial Black", sans-serif;
    font-weight: 400;
    color: var(--title-yellow);
    -webkit-text-stroke: 3px var(--title-line);
    paint-order: stroke fill;
    line-height: 1;
    letter-spacing: 1px;
  }
  .title--main { left: 22px; top: 14px; font-size: 54px; }
  .title--sub { left: 22px; top: 80px; font-size: 54px; }
  .byline {
    position: absolute;
    margin: 0;
    left: 320px;
    top: 80px;
    width: 270px;
    text-align: center;
    font-family: "Titan One", "Arial Black", sans-serif;
    color: var(--title-yellow);
    -webkit-text-stroke: 2px var(--title-line);
    paint-order: stroke fill;
    line-height: 1;
    transform: rotate(-4deg);
  }
  .byline__by { font-size: 14px; display: block; }
  .byline__name { font-size: 26px; display: block; }

  .intro-text {
    position: absolute;
    left: 30px;
    top: 194px;
    width: 590px;
    margin: 0;
    font-size: 20.5px;
    line-height: 1.2;
    text-align: center;
  }
  .call-text {
    position: absolute;
    left: 20px;
    top: 290px;
    width: 604px;
    margin: 0;
    font-size: 24px;
    line-height: 1.13;
    text-align: center;
  }
  .body-text {
    position: absolute;
    left: 20px;
    top: 414px;
    width: 590px;
    margin: 0;
    font-size: 20.5px;
    line-height: 1.2;
  }
  .topics {
    position: absolute;
    left: 20px;
    top: 558px;
    width: 280px;
    margin: 0;
    padding: 0;
    list-style: none;
    font-size: 16.5px;
    line-height: 1.26;
  }
  .results {
    position: absolute;
    left: 312px;
    top: 556px;
    width: 332px;
    height: 284px;
    background: var(--teal);
  }
  .results__label {
    position: absolute;
    margin: 0;
    font-size: 14px;
    color: var(--navy);
    white-space: nowrap;
  }
  .results__label--acid { left: 22px; top: 10px; }
  .results__label--during { left: 160px; top: 10px; }
  .results__label--after { left: 92px; top: 128px; }
  .results__photo {
    position: absolute;
    border: 2px solid #4a5a66;
  }
  .results__photo--acid { left: 14px; top: 32px; width: 124px; height: 84px; background: linear-gradient(135deg, #8a8f86 0%, #c9ccc4 45%, #6b705f 100%); }
  .results__photo--during { left: 172px; top: 32px; width: 124px; height: 84px; background: linear-gradient(135deg, #b9b4a8 0%, #e6e4dc 40%, #8d8676 100%); }
  .results__photo--after { left: 86px; top: 150px; width: 160px; height: 124px; background: linear-gradient(160deg, #b7b3a6 0%, #e8e8e2 40%, #6f6756 100%); }

  .footer-text {
    position: absolute;
    left: 10px;
    top: 846px;
    width: 624px;
    margin: 0;
    font-size: 19px;
    line-height: 1.25;
    text-align: center;
    color: var(--lime);
  }
</style>
</head>
<body>
<div class="canvas">
  <article class="flyer">
    <div class="band band--header"></div>
    <div class="band band--intro"></div>
    <div class="band band--call"></div>
    <div class="band band--body"></div>
    <div class="band band--footer"></div>

    <h1 class="title title--main">GLASS RESTORATION</h1>
    <h2 class="title title--sub">SEMINAR</h2>
    <p class="byline">
      <span class="byline__by">by</span>
      <span class="byline__name">" PANE MAVEN "</span>
      <span class="byline__name">LYLE BRANDT</span>
    </p>

    <p class="intro-text">Spend a day with The PaneMaven and learn how you can benefit from learning "Glass Restoration" and the many benefits to offering this service to your clients.</p>

    <p class="call-text">Ready to expand your business<br>and make some great money?<br>"DON'T WAIT" - Start offering your clients<br>Glass Restoration Services</p>

    <p class="body-text">Glass Restoration" is one of the most profitable "Add-On" businesses for the window cleaning industry and you now have an opportunity to learn from one of the industry leaders. Lyle Brandt will be offering a full day "hands-on" seminar on Glass Restoration.</p>

    <ul class="topics">
      <li>The seminar will cover:</li>
      <li>Glass Types</li>
      <li>Glass Damage</li>
      <li>Glass Coatings</li>
      <li>Glass Distortion &amp; Breakage</li>
      <li>Glass Restoration Systems</li>
      <li>Glass Restoration Procedures</li>
      <li>Customer Expectations</li>
      <li>Marketing and Pricing a job</li>
      <li>Hands on demonstrations</li>
      <li>And much much more.....</li>
      <li>And did I mention</li>
      <li>it will cover "Glass"?</li>
    </ul>

    <section class="results">
      <p class="results__label results__label--acid">ACID DAMAGE</p>
      <p class="results__label results__label--during">DURING RESTORATION</p>
      <div class="results__photo results__photo--acid" role="img" aria-label="Photo of window glass with acid etch damage"></div>
      <div class="results__photo results__photo--during" role="img" aria-label="Photo of window glass partway through restoration"></div>
      <p class="results__label results__label--after">AFTER RESTORATION</p>
      <div class="results__photo results__photo--after" role="img" aria-label="Photo of clear restored storefront glass"></div>
    </section>

    <p class="footer-text">Space will be limited, so you must register to attend<br>SEMINAR and LUNCH is FREE.</p>
  </article>
</div>
</body>
</html>
```